High School Rowing Club - duplicate example provided

Build web site based on example provided. We would like you to copy the general layout of the Corlinder rowing web site but insert our info (Maple Ridge Western).
Target Market(s)
High School Parents & Students
Industry/Entity Type
School
Number of Pages Required
5+ page
Font styles to use
Serif
Colors
Designer to choose colors to be used in the design.
Requirements
Must have
- Plug in for payment option (coinvale?) Parents will be making payments using this options.
- Online Registration Form - Please copy http://corlinderpaddlehub.com/ registration form inserting the basics. Please do not include their specific items at the bottom.
- Generally, Copy the format of http://corlinderpaddlehub.com/ to build our site.
Nice to have
- Include the photos we attached. Use "slider" format/style. Include our facebook page on the home/main page: Maple Ridge Western High School Rowing Team.
- Our content should work for 5 pages (tabs)
- Make sure to copy the green color from our current high school rowing website. http://www.mrwoars.org/

```html
<!DOCTYPE html>
<html lang="en">
<head>
<meta charset="utf-8">
<title>Maple Ridge Western Rowing</title>
<link rel="stylesheet" href="https://fonts.googleapis.com/css2?family=Oswald:wght@400;500;600&display=swap">
<style>
  :root {
    --green: #0d8a3a;
    --green-dark: #0b4a22;
    --green-deep: #06361a;
    --black: #000000;
    --charcoal: #242424;
    --white: #ffffff;
    --ink: #111111;
    --rule: #666666;
    --muted: #777777;
  }
  * { margin: 0; padding: 0; box-sizing: border-box; }
  html, body { width: 1200px; height: 1189px; overflow: hidden; }
  body {
    font-family: "Oswald", sans-serif;
    color: var(--white);
    background: var(--charcoal);
    position: relative;
    text-transform: uppercase;
  }
  .masthead {
    position: absolute; left: 0; top: 0; width: 1200px; height: 117px;
    background: linear-gradient(90deg, #063a16 0%, #0a5a24 45%, #0b6a2a 70%, #0a5222 100%);
    display: flex; align-items: center; justify-content: center;
  }
  .brand {
    font-weight: 600; font-size: 20px; letter-spacing: 1px; color: var(--white);
    display: flex; align-items: center; gap: 8px;
  }
  .brand-dot { width: 10px; height: 10px; border-radius: 50%; background: var(--white); }
  .main-nav {
    position: absolute; left: 0; top: 117px; width: 1200px; height: 36px;
    background: var(--black);
  }
  .main-nav a {
    position: absolute; top: 9px; transform: translateX(-50%);
    color: var(--white); text-decoration: none; font-size: 13px; font-weight: 500;
    line-height: 16px; padding-bottom: 2px; white-space: nowrap;
  }
  .main-nav a.active { border-bottom: 2px solid var(--green); }
  .hero {
    position: absolute; left: 0; top: 153px; width: 1200px; height: 562px;
    background: radial-gradient(ellipse at 50% 45%, #d9dbdb 0%, #c4c7c7 45%, #aeb2b1 75%, #9da1a0 100%);
  }
  .hero-title {
    position: absolute; left: 0; width: 1200px; top: 246px;
    text-align: center; color: var(--ink); font-weight: 600;
    font-size: 44px; line-height: 54px; letter-spacing: -0.5px;
  }
  .scroll-cue { position: absolute; left: 582px; top: 492px; }
  .lower {
    position: absolute; left: 0; top: 715px; width: 1200px; height: 376px;
    background: linear-gradient(180deg, #2b2b2b 0%, #232323 60%, #262626 100%);
  }
  .col { position: absolute; top: 70px; }
  .col-title { font-size: 20px; font-weight: 500; line-height: 26px; white-space: nowrap; }
  .col-title::after {
    content: ""; display: block; width: 69px; height: 2px; background: var(--green); margin-top: 4px;
  }
  .calendar { left: 108px; }
  .calendar ul { list-style: none; margin-top: 28px; }
  .calendar li { font-size: 13px; font-weight: 500; line-height: 33px; white-space: nowrap; }
  .news { left: 301px; width: 262px; }
  .news-item { margin-top: 34px; }
  .news-item + .news-item { margin-top: 26px; }
  .news-head { font-size: 13px; font-weight: 500; line-height: 22px; }
  .news-date { font-size: 12px; color: var(--green); margin-top: 5px; }
  .news-rule { border-top: 1px dashed #555; margin-top: 14px; width: 222px; }
  .photos { left: 587px; width: 251px; }
  .photo-grid {
    margin-top: 34px; display: grid; grid-template-columns: repeat(3, 78px);
    grid-auto-rows: 69px; gap: 9px 8px;
  }
  .photo-grid div:nth-child(1) { background: linear-gradient(135deg, #4d6a3c, #1f3b2b); }
  .photo-grid div:nth-child(2) { background: linear-gradient(135deg, #8a7b5c, #2b4a35); }
  .photo-grid div:nth-child(3) { background: linear-gradient(135deg, #9aa096, #3a4a40); }
  .photo-grid div:nth-child(4) { background: linear-gradient(135deg, #5b6b50, #1d2d23); }
  .photo-grid div:nth-child(5) { background: linear-gradient(135deg, #cfcfc8, #3f5a44); }
  .photo-grid div:nth-child(6) { background: linear-gradient(135deg, #7f8a68, #253a2c); }
  .btn-more {
    display: block; margin-top: 6px; height: 39px; background: var(--green);
    color: var(--white); text-decoration: none; text-align: center;
    font-size: 14px; font-weight: 500; line-height: 39px;
  }
  .apparel { left: 866px; }
  .apparel-box {
    margin-top: 34px; width: 224px; height: 192px; background: var(--black);
    border: 1px solid var(--green); padding: 30px 0 0 19px;
  }
  .apparel-box a {
    display: flex; align-items: center; gap: 10px; color: var(--white);
    font-size: 12px; font-weight: 500; height: 47px; white-space: nowrap;
  }
  .apparel-box a span { text-decoration: underline; }
  .footer {
    position: absolute; left: 0; top: 1091px; width: 1200px; height: 98px;
    border-top: 1px dashed var(--rule);
  }
  .footer-copy { position: absolute; left: 108px; top: 50px; font-size: 12px; font-weight: 500; white-space: nowrap; }
  .footer-line { position: absolute; top: 60px; border-top: 1px dashed var(--muted); }
  .footer-brand {
    position: absolute; left: 0; width: 1200px; top: 45px; text-align: center;
    font-size: 17px; font-weight: 600; letter-spacing: 0.5px;
  }
  .footer-contact {
    position: absolute; left: 938px; top: 50px; font-size: 12px; font-weight: 500;
    display: flex; align-items: center; gap: 12px; white-space: nowrap;
  }
  .social { width: 10px; height: 10px; border-radius: 50%; background: var(--muted); }
  .social:first-of-type { background: var(--green); }
</style>
</head>
<body>
  <header class="masthead">
    <div class="brand"><span class="brand-dot"></span>Maple Ridge Western</div>
  </header>

  <nav class="main-nav">
    <a class="active" href="#" style="left:415px">New or Interested</a>
    <a href="#" style="left:545px">Coaches</a>
    <a href="#" style="left:664px">Parent Info</a>
    <a href="#" style="left:793px">Sponsorships</a>
  </nav>

  <section class="hero" role="img" aria-label="Rowing crew in a boat on a misty river at dawn">
    <h1 class="hero-title">We are a high school<br>rowing club</h1>
    <svg class="scroll-cue" width="36" height="36" viewBox="0 0 36 36" aria-label="Scroll down">
      <circle cx="18" cy="18" r="18" fill="var(--green-deep)"/>
      <circle cx="18" cy="18" r="14" fill="none" stroke="#5fae78" stroke-width="1"/>
      <path d="M12 13 L18 23 L24 13" fill="none" stroke="#ffffff" stroke-width="1.6"/>
    </svg>
  </section>

  <section class="lower" role="img" aria-label="Darkened photo of rowers on the water">
    <div class="col calendar">
      <h2 class="col-title">Calendar</h2>
      <ul>
        <li>Eeg.a.than</li>
        <li>Belted Galbway</li>
        <li>LVHS Inviteddie Cup</li>
        <li>Laddie Cup</li>
        <li>Midwest</li>
        <li>State Championship</li>
      </ul>
    </div>

    <div class="col news">
      <h2 class="col-title">Latest News</h2>
      <article class="news-item">
        <p class="news-head">Come celebrate our 2017 state champions at the high school assembly</p>
        <p class="news-date">Thursday, September 28 at 1:50 P.M</p>
        <div class="news-rule"></div>
      </article>
      <article class="news-item">
        <p class="news-head">Fall conditioning is open to all Maple Ridge Western varsity rowers</p>
        <p class="news-date">Tuesday, September 12 at 1:50 P.M</p>
      </article>
    </div>

    <div class="col photos">
      <h2 class="col-title">Crew Photos</h2>
      <div class="photo-grid">
        <div role="img" aria-label="Team members in green jackets"></div>
        <div role="img" aria-label="Rowers gathered outdoors"></div>
        <div role="img" aria-label="Crew carrying a boat"></div>
        <div role="img" aria-label="Rower preparing equipment"></div>
        <div role="img" aria-label="Parent and rower together"></div>
        <div role="img" aria-label="Rowers at the dock"></div>
      </div>
      <a class="btn-more" href="#">View More Photos</a>
    </div>

    <div class="col apparel">
      <h2 class="col-title">Team Apparel</h2>
      <div class="apparel-box">
        <a href="#"><svg width="20" height="24" viewBox="0 0 20 24"><path d="M2 1 H13 L18 6 V23 H2 Z M13 1 V6 H18" fill="none" stroke="var(--green)" stroke-width="1.3"/></svg><span>Men's unisuit sizing info</span></a>
        <a href="#"><svg width="20" height="24" viewBox="0 0 20 24"><path d="M2 1 H13 L18 6 V23 H2 Z M13 1 V6 H18" fill="none" stroke="var(--green)" stroke-width="1.3"/></svg><span>Crew apparel order form</span></a>
        <a href="#"><svg width="20" height="24" viewBox="0 0 20 24"><path d="M2 1 H13 L18 6 V23 H2 Z M13 1 V6 H18" fill="none" stroke="var(--green)" stroke-width="1.3"/></svg><span>Women's unisuit sizing info.</span></a>
      </div>
    </div>
  </section>

  <footer class="footer">
    <p class="footer-copy">© 2017 Company Name | All Rights Reserved</p>
    <div class="footer-line" style="left:346px;width:150px"></div>
    <div class="footer-brand">Maple Ridge Western</div>
    <div class="footer-line" style="left:704px;width:151px"></div>
    <div class="footer-contact">
      <span>Get in touch</span>
      <i class="social"></i><i class="social"></i><i class="social"></i><i class="social"></i>
    </div>
  </footer>
</body>
</html>
```